Marketing genius wanted: Independant audiologists need generic ad customized w/ powerful call to act

Hello! For the first time, we are moving away from advertising product (hearing aids) and starting to focus on the importance of hearing healthcare using non-product advertisements. We need the ads to be customized to our practice (easy part) but we also want to have a strong call to action to sell hearing aids (tricky part). We want to bring in customers by selling our expertise and the importance of hearing healthcare instead of advertising some "widget" like everyone else! Please use any info off our website: www.palvermoorlistening.com to get a feel for our practice. Good luck! This is a project for the most creative among you!

Target Market(s)

Baby Boomers (65 year olds +) through elderly.

Industry/Entity Type

Marketing

Requirements
Must have
• Please use the images attached as the base for the ads. We need to still bring customers in to our office to sell hearing aids but we want to do that using our expertise and not advertising a manufacturer's hearing aids. The trick is to get people to respond without using price discounts or other gimmicks. We want to keep the ads very professional and trustworthy. Thank you!!
Should not have
• Do not include anything about price or discounts.

```html
<!DOCTYPE html>
<html lang="en">
<head>
<meta charset="utf-8">
<title>Palvermoor Listening – Print Spread</title>
<link href="https://fonts.googleapis.com/css2?family=Quicksand:wght@400;500;600;700&display=swap" rel="stylesheet">
<style>
  :root{
    --navy:#1c3f5f;
    --teal:#2aa697;
    --panel:#edf5f3;
    --page:#ffffff;
    --stage:#f1f1f1;
    --beige:#e9e4df;
    --body:#2f4a63;
  }
  *{margin:0;padding:0;box-sizing:border-box}
  html,body{width:1200px;height:1000px;overflow:hidden;background:var(--stage);font-family:"Quicksand",sans-serif;color:var(--body)}
  .spread{position:absolute;left:32px;top:246px;width:1122px;height:506px;box-shadow:0 6px 18px rgba(0,0,0,.18);background:var(--page)}
  /* left page */
  .cover{position:absolute;left:0;top:0;width:561px;height:506px;overflow:hidden;background:var(--beige)}
  .cover-photo{position:absolute;inset:0;
    background:
      radial-gradient(ellipse 260px 200px at 390px 360px,rgba(214,176,140,.75) 0%,rgba(214,176,140,0) 100%),
      radial-gradient(ellipse 240px 220px at 170px 330px,rgba(160,140,125,.7) 0%,rgba(160,140,125,0) 100%),
      linear-gradient(180deg,#ebe7e3 0%,#e8e3de 38%,#d9cbbf 62%,#cdb9a8 100%)}
  .brand{position:absolute;display:flex;align-items:center;gap:7px;color:var(--navy);font-weight:600;line-height:1;white-space:nowrap}
  .brand-dot{border-radius:50%;background:var(--teal);flex:none}
  .cover .brand{left:26px;top:38px;font-size:18px}
  .cover .brand-dot{width:28px;height:28px}
  .cover-headline{position:absolute;left:263px;top:70px;font-size:15.5px;line-height:1.15;color:var(--navy);font-weight:500}
  .cover-headline b{font-weight:700}
  /* right page */
  .inner{position:absolute;left:561px;top:0;width:561px;height:506px}
  .inner .brand{left:12px;top:16px;font-size:12px}
  .inner .brand-dot{width:20px;height:20px}
  .tagline{position:absolute;right:304px;top:56px;text-align:right;font-size:21px;line-height:1.05;color:var(--navy);font-weight:500}
  .tagline span{color:var(--teal)}
  .team-photo{position:absolute;left:282px;top:0;width:261px;height:138px;
    background:
      radial-gradient(ellipse 80px 110px at 70px 100px,rgba(70,80,105,.55) 0%,rgba(70,80,105,0) 100%),
      radial-gradient(ellipse 80px 110px at 195px 100px,rgba(196,140,112,.55) 0%,rgba(196,140,112,0) 100%),
      linear-gradient(90deg,#e6e7e4 0%,#ece9e5 50%,#eef0ef 100%)}
  .col{position:absolute;font-size:4.9px;line-height:1.5}
  .col h3{font-size:8.5px;font-weight:700;color:var(--teal);margin-bottom:3px;text-transform:uppercase}
  .col p{margin-bottom:4px;text-align:justify}
  .col-about{left:20px;top:151px;width:142px}
  .col-mid{left:172px;top:151px;width:152px}
  .services{margin-bottom:5px}
  .services li{list-style:none;margin-bottom:1.5px;font-weight:600}
  .services li::before{content:"› ";color:var(--teal)}
  .quote{background:var(--panel);padding:3px 5px;margin-bottom:6px;line-height:1.45}
  .quote .by{text-align:right;font-weight:700;margin-top:2px}
  .quote::before{content:"“ ";color:var(--teal);font-weight:700;font-size:7px}
  .contact-bar{position:absolute;left:0;top:443px;width:164px;height:41px;background:var(--navy);color:#fff;padding:3px 10px}
  .contact-bar .phone{font-size:13px;font-weight:600}
  .contact-bar .addr{font-size:5.5px;line-height:1.3}
  .quiz{position:absolute;left:336px;top:146px;width:207px;height:259px;background:var(--panel);padding:5px 6px}
  .quiz h2{font-size:12.5px;color:var(--navy);font-weight:700;margin-bottom:7px}
  .quiz ul{list-style:none;font-size:4.9px;line-height:1.35}
  .quiz li{margin-bottom:4.2px;padding-left:8px;position:relative}
  .quiz li::before{content:"";position:absolute;left:0;top:1px;width:4px;height:4px;border-radius:50%;background:var(--teal)}
  .quiz .note{font-size:4.9px;margin:0 0 5px}
  .cta{position:absolute;left:342px;top:413px;width:200px}
  .cta h2{font-size:11.5px;line-height:1.05;color:var(--teal);font-weight:700}
  .cta p{font-size:4.9px;line-height:1.4;margin-top:3px}
  .web-bar{position:absolute;left:336px;top:464px;width:225px;height:20px;background:var(--navy);color:#fff;font-size:12px;font-weight:500;padding:3px 4px}
</style>
</head>
<body>
<main class="spread">
  <section class="cover">
    <div class="cover-photo" role="img" aria-label="Photo: an older woman laughing and whispering to a smiling young woman"></div>
    <div class="brand"><span class="brand-dot"></span>Palvermoor Listening</div>
    <p class="cover-headline">When you <b>mishear</b>, you <b>miss out</b><br>on important <b>pieces of your life.</b></p>
  </section>

  <section class="inner">
    <div class="brand"><span class="brand-dot"></span>Palvermoor Listening</div>
    <h1 class="tagline">We listen<br>SO <span>YOU CAN HEAR</span></h1>
    <div class="team-photo" role="img" aria-label="Photo: two smiling audiologists in business attire"></div>

    <div class="col col-about">
      <h3>About us</h3>
      <p>Selecting a qualified hearing healthcare provider is one of the most important keys to your success. Proper hearing aid recommendation and fitting is highly dependent on the judgment and skill of the professional selecting your hearing aids. Furthermore, you will be forging a long term relationship with this individual and practice, just as you do your doctor or dentist.</p>
      <p>Our audiologists are Doctors of Audiology, or are candidates for the doctorate degree, which means they have received, or are working toward, an AuD (Doctorate of Audiology) degree from an accredited university graduate program. Doctors of Audiology provide in depth diagnosis of auditory pathology, make recommendations, and provide non-medical treatment (typically hearing aid fitting and hearing loss counseling) or make referral for medical treatment.</p>
      <p>In contrast, hearing aid dispensers (typically located at Chainline Audio, Soundmart, Bulkway and shopping malls) are licensed in hearing aid dispensing only and can do hearing screening solely for the purpose of fitting a hearing aid. The entry level requirement for hearing instrument dispensers in the state of Washington is a two year associates degree.</p>
      <p>In order to stay abreast of rapidly evolving hearing aid technological advances, each of our audiologists is committed to a minimum of 25 hours annually of continuing education.</p>
      <p>When you call our office, you will most likely speak with our patient care coordinator, Maren Holt, who has a hearing loss herself. Her ability to relate to those with hearing loss affords us a unique appreciation of your hearing challenges.</p>
      <p>If you are looking for a qualified, experienced hearing healthcare provider, feel free to print out our Practice Comparison Form while doing your research.</p>
      <p>If you would like to learn more about our practice, please proceed to Meet Our Staff.</p>
    </div>

    <div class="contact-bar">
      <div class="phone">(206) 555-0148</div>
      <div class="addr">4410 Alder Crest Ave Ste 12<br>Seattle WA 98100</div>
    </div>

    <div class="col col-mid">
      <h3>Services</h3>
      <ul class="services">
        <li>Battery Sales</li>
        <li>Diagnostic Hearing Tests</li>
        <li>Custom Earmolds and Earplugs</li>
        <li>Assistive Listening Devices</li>
        <li>Musicians Earplugs and Monitors</li>
        <li>Hearing Aid Dispensing and Fitting</li>
        <li>Hearing Aid Repairs</li>
        <li>In Office Services</li>
        <li>Live Speech Mapping</li>
        <li>Tympanometry</li>
      </ul>
      <h3>Satisfaction guaranteed</h3>
      <p>At Palvermoor Listening, YOU come first. We are committed to spending as much time as you need to feel comfortable with your treatment plan. We have no allegiances to hearing aid manufacturers nor are we under any pressure to fit you with the "hearing aid of the month".</p>
      <h3>Testimonials</h3>
      <div class="quote">I am very pleased with my Vessa Pro aids and the warm and expert service from Dr. Varga. This latest pair of aids is the first time I have bought two at the same time – wish I had done this years ago. It is amazing how well the aids work in tandem with each other and without adjusting on my part. Superb experience!<div class="by">– Dana R.</div></div>
      <div class="quote">I've had a wonderful experience with Dr. Lindqvist and Palvermoor Listening. She and her staff are thoroughly attentive and patient. My hearing aids are fabulous! I'm so pleased that I came to Palvermoor Listening!<div class="by">– Leah P.</div></div>
      <div class="quote">Great hearing aids! I can hear much, much better now. It makes a difference. Nice to talk to friends and family again!<div class="by">– Greta T.</div></div>
    </div>

    <aside class="quiz">
      <h2>Do you think?</h2>
      <ul>
        <li>Do I have a hearing loss that needs to be evaluated by a professional?</li>
      </ul>
      <p class="note">If you answer yes to more than two of the following questions, you should have your hearing evaluated further by a certified audiologist.</p>
      <ul>
        <li>Do you have a problem hearing over the telephone?</li>
        <li>Do you hear better through one ear than the other when you are on the telephone?</li>
        <li>Do you have trouble following the conversation with two or more people talking at the same time?</li>
        <li>Do people complain that you turn the TV volume up too high?</li>
        <li>Do you have to strain to understand conversation?</li>
        <li>Do you have trouble hearing in a noisy background?</li>
        <li>Do you have trouble hearing in restaurants?</li>
        <li>Do you have dizziness, pain, or ringing in your ears?</li>
        <li>Do you find yourself asking people to repeat themselves?</li>
        <li>Do family members or coworkers remark about your missing what has been said?</li>
        <li>Do many people you talk to seem to mumble (or not speak clearly)?</li>
        <li>Do you misunderstand what others are saying and respond inappropriately?</li>
        <li>Do you have trouble understanding the speech of women and children?</li>
        <li>Do people get annoyed because you misunderstand what they say?</li>
      </ul>
    </aside>

    <div class="cta">
      <h2>SCHEDULE YOUR<br>APPOINTMENT TODAY</h2>
      <p>We take pride in helping you and your family with their hearing health care needs. Contact us today to schedule your appointment and discover how we can help you.</p>
    </div>
    <div class="web-bar">www.palvermoorlistening.com</div>
  </section>
</main>
</body>
</html>
```